BUSINESS CARD FOR GUITAR SCHOOL

I would like to design a business card for my Guitar Music School. The school is called "Pluck & Lantern".

The card should be yellow.

Target Market(s)

18-35 years old

Industry/Entity Type

School

Contact Information for Business Card

I would like to design a business card for my Guitar Music School. The school is called "Pluck & Lantern". The card should be yellow.

Card must be consistent with my website design: www.pluckandlantern.com.sg

Requirements
Must have
• 1) Name of Company
• 2) Company Logo
• 3) Name of Employee
• 4) Position of Employee
• 5) Contact Number
• 6) Address
Nice to have
• Creative Design
• Card must be consistent with my website design: www.pluckandlantern.com.sg
Should not have
• Boring Design

```html
<!DOCTYPE html>
<html lang="en">
<head>
<meta charset="utf-8">
<title>Pluck &amp; Lantern – Business Card</title>
<link rel="stylesheet" href="https://fonts.googleapis.com/css2?family=Arimo:wght@700&family=Mulish:ital,wght@0,400;0,700;0,800;1,400&display=swap">
<style>
  :root {
    --page: #ffffff;
    --paper: #ebeced;
    --yellow: #fcbf27;
    --yellow-deep: #eaa911;
    --ink: #333333;
    --shadow: rgba(0,0,0,0.18);
  }
  * { box-sizing: border-box; margin: 0; padding: 0; }
  html, body {
    width: 1048px; height: 1200px; overflow: hidden;
    background: var(--page);
    font-family: "Mulish", "Century Gothic", sans-serif;
    color: var(--ink);
  }
  .canvas { position: relative; width: 1048px; height: 1200px; }
  .card {
    position: absolute; left: 125px; width: 786px; height: 464px;
    background: var(--paper); overflow: hidden;
    box-shadow: 0 4px 14px var(--shadow);
  }
  .card--front { top: 96px; }
  .card--back { top: 644px; }
  .card__wave { position: absolute; inset: 0; width: 100%; height: 100%; }
  .card__wave .band { fill: var(--yellow); }
  .card__wave .edge { fill: none; stroke: var(--ink); stroke-width: 3; }

  .front__url {
    position: absolute; top: 70px; left: 0; width: 100%; text-align: center;
    font-family: "Arimo", Arial, sans-serif; font-weight: 700; font-size: 26px;
  }
  .brand {
    position: absolute; left: 262px; top: 212px;
    font-weight: 800; font-size: 76px; line-height: 0.86; letter-spacing: -2px;
    color: var(--ink);
  }
  .brand__tagline {
    position: absolute; left: 404px; top: 360px;
    font-size: 17px; font-weight: 700; color: var(--ink);
  }
  .staff-art {
    position: absolute; border-radius: 40%;
    background: radial-gradient(ellipse at center, var(--yellow-deep) 0%, var(--yellow) 72%);
  }
  .card--front .staff-art { left: 12px; top: 280px; width: 268px; height: 172px; }
  .card--back .staff-art { left: 508px; top: 26px; width: 272px; height: 116px; }

  .person { position: absolute; left: 76px; top: 72px; }
  .person__name { font-weight: 700; font-size: 25px; }
  .person__role { font-size: 25px; margin-top: 4px; }

  .contacts { position: absolute; left: 78px; top: 214px; list-style: none; font-size: 22px; }
  .contacts li { display: flex; align-items: flex-start; height: 36px; }
  .contacts li.contacts__address { height: auto; margin-top: 6px; line-height: 30px; }
  .contacts svg { width: 22px; height: 22px; margin: 4px 10px 0 0; flex: none;
    fill: none; stroke: var(--ink); stroke-width: 1.8; }
  .contacts .note { font-style: italic; font-size: 19px; }
</style>
</head>
<body>
<div class="canvas">

  <section class="card card--front">
    <svg class="card__wave" viewBox="0 0 720 424" preserveAspectRatio="none" aria-hidden="true">
      <path class="band" d="M0 144 C90 148 170 170 203 217 C214 190 214 152 262 142 C400 132 560 134 720 142 V424 H0 Z"/>
      <path class="edge" d="M0 144 C90 148 170 170 203 217 C214 190 214 152 262 142 C400 132 560 134 720 142"/>
    </svg>
    <p class="front__url">www.pluckandlantern.com.sg</p>
    <div class="staff-art" role="img" aria-label="Swirling music staff with treble clef and notes"></div>
    <h1 class="brand">Pluck &amp;<br>Lantern</h1>
    <p class="brand__tagline">Guiding Every Chord to New Heights</p>
  </section>

  <section class="card card--back">
    <svg class="card__wave" viewBox="0 0 720 424" preserveAspectRatio="none" aria-hidden="true">
      <path class="band" d="M0 0 H720 V155 L522 240 C516 205 502 184 470 178 C380 163 250 145 0 155 Z"/>
      <path class="edge" d="M0 155 C250 145 380 163 470 178 C502 184 516 205 522 240 L720 155"/>
    </svg>
    <div class="staff-art" role="img" aria-label="Swirling music staff with treble clef and notes"></div>
    <div class="person">
      <p class="person__name">Name Surname</p>
      <p class="person__role">Position</p>
    </div>
    <ul class="contacts">
      <li><svg viewBox="0 0 24 24"><path d="M6 3l3 4-2 2c1 3 4 6 7 7l2-2 4 3-2 3C10 20 4 14 3 5z"/></svg>+65 6100 4821</li>
      <li><svg viewBox="0 0 24 24"><rect x="6" y="2" width="12" height="20" rx="2"/><path d="M10 18h4"/></svg>+65 8200 1357</li>
      <li><svg viewBox="0 0 24 24"><rect x="2" y="5" width="20" height="14"/><path d="M2 5l10 8 10-8"/></svg>name@pluckandlantern.com.sg</li>
      <li><svg viewBox="0 0 24 24"><circle cx="12" cy="12" r="10"/><ellipse cx="12" cy="12" rx="4" ry="10"/><path d="M2 12h20M4 7h16M4 17h16"/></svg>www.pluckandlantern.com.sg</li>
      <li class="contacts__address"><svg viewBox="0 0 24 24"><path d="M2 10l10-6 10 6M4 10v10h16V10M9 20v-6h6v6"/></svg><span>27 Kallang Crescent Harbour Building B #05-03<br>Singapore 418842 <span class="note">(Strictly By Appointment Only)</span></span></li>
    </ul>
  </section>

</div>
</body>
</html>
```